依頼詳細
●デザインの要望
・少し温かみ、やわらかさのあるデザイン(まるっこすぎない)
※参考例:poruくらいのやわらかさ
・そのほかの色については特に指定なし(現在の青は入れなくてOKです)
⇒カラフルにするかどうかもデザインの中で考えて頂いて結構です
・現在のアプリにある下記のボタンを全て実装する
※投稿ボタン、画面更新ボタン、履歴ボタン、オプションボタン、カテゴリ選択ボタン の5個
・投稿が表示されるマス目は正方形だけでなく長方形等もまぜてほしい
※現在は正方形オンリーですが、縦に2個くっつけたものや横に2個くっつけたものが入ってきたりするデザイン
⇒アプリ:Tiledeck の記事一覧画面のようなイメージ
・zelvonなのでzvos7のフラットなイメージ(がっつり立体的にはしてほしくないです)

●納品物
PSDファイル1個(zelvonで使用する倍のサイズの 1920x1280 くらいで作ってください)
可能であればレイヤーのあるPNGファイル(可能であればで結構です)

サイトURL
https://apps.trovenlo.jp/jp/app/id518203764?mt=8
ページ数
1ページ
希望イメージ
シンプル 複雑
単色 カラフル
暗い 明るい
日常 高級
遊び心 厳粛
未来的 伝統的
女性的 男性的
希望する色
小豆色や薄い茶色等温かみのある色全般
納品ファイル
• フォトショップ形式 (.psd)
• PNG形式 (.png)
補足説明
■ 選んだ理由

やわらかいテイストでかつ既存の青をさし色に入れて頂けたこと、
またプラスアルファとしてスプラッシュスクリーンをご提示いただけたため、
より実装後のアプリのイメージがわくことができました。

■ 提案者全員のお礼・コメント

たくさんのご提案ありがとうございました。
特にUIそのものまで提案して頂けたりと非常にこちらとしても勉強になる案件となりました。

上部のバーのデザインや、吹き出し型のデザイン、カラフル、マット等
かなり悩ませていただきました。
最終的にはより女性的で、かつ落ち着いている
という部分を基準に選ぶことにしました。

本アプリは今後もどんどん改良を加える予定のため、
また機会が有りましたら是非宜しくお願い致します。

```html
<!DOCTYPE html>
<html lang="ja">
<head>
<meta charset="utf-8">
<title>タイル一覧画面</title>
<link href="https://fonts.googleapis.com/css2?family=Noto+Sans+JP:wght@400;500&display=swap" rel="stylesheet">
<style>
  :root {
    --paper: #ffffff;
    --cocoa: #7b4b2d;
    --caramel: #c98b5f;
    --latte: #d49a6c;
    --peach: #fbd5b4;
    --apricot: #f6a55f;
    --ink-dark: #5b3a27;
    --ink-light: #ffffff;
    --tabbar: #fcefe8;
    --tab-ink: #7a5646;
    --status-ink: #111111;
  }
  * { box-sizing: border-box; margin: 0; padding: 0; }
  html, body { width: 677px; height: 1200px; overflow: hidden; }
  body {
    background: var(--paper);
    font-family: "Noto Sans JP", sans-serif;
    position: relative;
  }
  .status-bar {
    position: absolute; left: 0; top: 0; width: 677px; height: 45px;
    background: var(--paper); color: var(--status-ink);
    font-size: 24px; font-weight: 500;
    display: flex; align-items: center; justify-content: space-between;
    padding: 0 12px;
  }
  .status-left, .status-right { display: flex; align-items: center; gap: 8px; width: 230px; }
  .status-right { justify-content: flex-end; }
  .signal { display: flex; gap: 3px; }
  .signal i { width: 10px; height: 10px; border-radius: 50%; background: var(--status-ink); display: block; }
  .signal i.off { background: none; border: 1.5px solid var(--status-ink); }
  .battery { width: 48px; height: 20px; border: 2px solid var(--status-ink); border-radius: 4px; padding: 2px; position: relative; }
  .battery::before { content: ""; display: block; height: 100%; background: var(--status-ink); border-radius: 1px; }
  .battery::after { content: ""; position: absolute; right: -6px; top: 5px; width: 3px; height: 7px; background: var(--status-ink); }

  .feed { position: absolute; left: 0; top: 45px; width: 677px; height: 1083px; overflow: hidden; }
  .tile {
    position: absolute; padding: 14px 16px;
    font-size: 22px; line-height: 1.45; letter-spacing: 0.02em;
    overflow: hidden; color: var(--ink-dark);
  }
  .tile--edge { padding-left: 136px; white-space: nowrap; }
  .tile.is-centered { display: flex; align-items: center; justify-content: center; text-align: center; }
  .tile.is-middle { display: flex; align-items: center; }
  .tile--paper { background: var(--paper); }
  .tile--cocoa { background: var(--cocoa); color: var(--ink-light); }
  .tile--caramel { background: var(--caramel); color: var(--ink-light); }
  .tile--latte { background: var(--latte); color: var(--ink-light); }
  .tile--peach { background: var(--peach); }
  .tile--apricot { background: var(--apricot); color: var(--ink-light); }

  .tab-bar {
    position: absolute; left: 0; top: 1128px; width: 677px; height: 72px;
    background: var(--tabbar); border-top: 1px solid #f1dcd0;
    display: flex; justify-content: space-around; align-items: center;
  }
  .tab { display: flex; flex-direction: column; align-items: center; gap: 2px; width: 120px; color: var(--tab-ink); font-size: 18px; line-height: 1.2; font-weight: 500; }
  .tab svg { width: 34px; height: 34px; }
</style>
</head>
<body>
  <header class="status-bar">
    <div class="status-left">
      <span class="signal"><i></i><i></i><i></i><i></i><i class="off"></i></span>
      <span>Kumotel</span>
      <svg width="24" height="18" viewBox="0 0 24 18"><path d="M2 6a14 14 0 0 1 20 0M5.5 9.5a9 9 0 0 1 13 0M9 13a4 4 0 0 1 6 0" fill="none" stroke="#111" stroke-width="2.4" stroke-linecap="round"/><circle cx="12" cy="16" r="1.6" fill="#111"/></svg>
    </div>
    <div class="status-time">4:21 PM</div>
    <div class="status-right">
      <span>100%</span>
      <span class="battery"></span>
    </div>
  </header>

  <main class="feed">
    <article class="tile tile--paper tile--edge" style="left:-120px;top:0;width:233px;height:226px;">k のデザ<br>ェーフラッ</article>
    <article class="tile tile--caramel" style="left:117px;top:0;width:233px;height:226px;">最近 Chirpa アップデートしてないんだけど、アップデート</article>
    <article class="tile tile--peach" style="left:354px;top:0;width:226px;height:452px;">ふとしたときにすごく好きだなって思うけど、近くにいるわけじゃないから街でカップル見るとつらい<br>あんな風に外歩きたいよ</article>
    <article class="tile tile--apricot" style="left:584px;top:0;width:226px;height:226px;">会いた<br>一緒に</article>

    <article class="tile tile--cocoa is-middle" style="left:-120px;top:230px;width:470px;height:222px;padding-left:130px;">招待状の印刷が終わらない…。ギターの練習がこの２日出来なかったよ。</article>
    <article class="tile tile--paper is-middle" style="left:584px;top:230px;width:226px;height:222px;">お金が</article>

    <article class="tile tile--latte tile--edge" style="left:-120px;top:456px;width:233px;height:221px;">k のデザ<br>ェーフラッ</article>
    <article class="tile tile--paper" style="left:117px;top:456px;width:233px;height:221px;">裏 Talkin って目的の人の Talkin が全部見れるんだー。彼氏には</article>
    <article class="tile tile--apricot is-centered" style="left:354px;top:456px;width:226px;height:221px;">雨ふっとる</article>
    <article class="tile tile--cocoa is-middle" style="left:584px;top:456px;width:226px;height:221px;">好きで<br>ずっと</article>

    <article class="tile tile--paper tile--edge" style="left:-120px;top:682px;width:233px;height:221px;">文のここが<br>とかテレ<br>するの。</article>
    <article class="tile tile--cocoa is-middle" style="left:117px;top:682px;width:233px;height:221px;">あの人とお話ししたい。。</article>
    <article class="tile tile--paper is-middle" style="left:354px;top:682px;width:456px;height:221px;">高学歴「なのに」ワーキングプアなのではなく、高学歴「だから」ワーキングプアなのでは。</article>

    <article class="tile tile--paper tile--edge" style="left:-120px;top:907px;width:233px;height:200px;">ります<br>すから<br>と起きる</article>
    <article class="tile tile--peach" style="left:117px;top:907px;width:233px;height:200px;">学校休むとかさぼるとか<br>行く意味ないなね?</article>
    <article class="tile tile--caramel is-centered" style="left:354px;top:907px;width:226px;height:200px;">返事してよ。</article>
    <article class="tile tile--apricot is-centered" style="left:584px;top:907px;width:226px;height:200px;justify-content:flex-start;">明日</article>
  </main>

  <nav class="tab-bar">
    <div class="tab">
      <svg viewBox="0 0 40 40"><path d="M8 32l2-8L26 8l6 6-16 16z" fill="var(--tab-ink)"/><path d="M8 32l8-2" stroke="#fcefe8" stroke-width="1.5"/></svg>
      <span>投稿</span>
    </div>
    <div class="tab">
      <svg viewBox="0 0 40 40"><path d="M29 13A11 11 0 1 0 31 24" fill="none" stroke="var(--tab-ink)" stroke-width="5"/><path d="M23 5h11v11z" fill="var(--tab-ink)"/></svg>
      <span>更新</span>
    </div>
    <div class="tab">
      <svg viewBox="0 0 40 40"><g fill="var(--tab-ink)"><circle cx="20" cy="20" r="11"/><rect x="17" y="4" width="6" height="32" rx="1"/><rect x="4" y="17" width="32" height="6" rx="1"/><rect x="17" y="4" width="6" height="32" rx="1" transform="rotate(45 20 20)"/><rect x="17" y="4" width="6" height="32" rx="1" transform="rotate(-45 20 20)"/></g><circle cx="20" cy="20" r="4.5" fill="var(--tabbar)"/></svg>
      <span>オプション</span>
    </div>
    <div class="tab">
      <svg viewBox="0 0 40 40"><g fill="var(--tab-ink)"><rect x="5" y="7" width="6" height="6"/><rect x="5" y="17" width="6" height="6"/><rect x="5" y="27" width="6" height="6"/><rect x="14" y="8" width="21" height="4"/><rect x="14" y="18" width="21" height="4"/><rect x="14" y="28" width="21" height="4"/></g></svg>
      <span>履歴</span>
    </div>
    <div class="tab">
      <svg viewBox="0 0 40 40"><g fill="none" stroke="var(--tab-ink)" stroke-width="2.5"><rect x="5" y="5" width="8" height="8"/><rect x="16" y="5" width="8" height="8"/><rect x="27" y="5" width="8" height="8"/><rect x="5" y="16" width="8" height="8"/><rect x="16" y="16" width="8" height="8"/><rect x="27" y="16" width="8" height="8"/><rect x="5" y="27" width="8" height="8"/><rect x="16" y="27" width="8" height="8"/><rect x="27" y="27" width="8" height="8"/></g></svg>
      <span>カテゴリ</span>
    </div>
  </nav>
</body>
</html>
```